Talvero Engineering & Management Services Website

A professional website design that outlines Engineering and Management Services. The website is to be colour coordinated with the current logo (see attached). The webpage needs to be compatible with Wordpress to allow for easy changes to be made to the website for the user.
Required tabs for the page include:
- Civil Engineering
- Structural Engineering
- Project Management
- Business Management
- Project Controls
- Drafting
- Contact Us

Clean and efficient website that matches the services provided by the business.

Target Market(s)

New Customers to a very competitive market

Industry/Entity Type

Engineering

Number of Pages Required

5+ page

Requirements
Must have
• Clean with large stock photos

```html
<!DOCTYPE html>
<html lang="en">
<head>
<meta charset="utf-8">
<title>Talvero Engineering &amp; Management Services</title>
<link href="https://fonts.googleapis.com/css2?family=Open+Sans:wght@300;400;600;700&display=swap" rel="stylesheet">
<style>
:root{
  --orange:#f07b1d;
  --orange-dark:#d9650c;
  --ink:#3b3b3b;
  --muted:#8a8a8a;
  --light:#f2f2f2;
  --line:#e2e2e2;
  --footer:#2e2e2e;
  --footer-deep:#232323;
  --white:#ffffff;
}
*{box-sizing:border-box;margin:0;padding:0}
html,body{width:1200px;height:2752px;overflow:hidden;background:var(--white)}
body{font-family:"Open Sans",Arial,sans-serif;color:var(--ink);position:relative}
.wrap{width:1040px;margin:0 auto;position:relative}

/* header */
.topbar{position:absolute;top:0;left:0;width:1200px;height:132px;display:flex;align-items:center}
.topbar .wrap{display:flex;align-items:center;justify-content:space-between}
.brand{display:flex;align-items:center;gap:14px}
.brand-dot{width:44px;height:44px;border-radius:50%;background:var(--orange)}
.brand-name{font-size:26px;font-weight:700;color:var(--ink);letter-spacing:1px}
.top-right{display:flex;align-items:center;gap:28px}
.socials{display:flex;gap:8px}
.socials span{width:26px;height:26px;border-radius:50%;background:var(--orange)}
.socials span:nth-child(2){background:#3b5998}
.socials span:nth-child(3){background:#888}
.contact-mini{font-size:14px;line-height:22px;color:var(--muted)}
.contact-mini .phone{color:var(--orange);font-weight:600;font-size:16px}
.contact-mini svg{vertical-align:-3px;margin-right:6px}

.nav{position:absolute;top:132px;left:0;width:1200px;height:44px;background:var(--orange)}
.nav ul{list-style:none;display:flex;justify-content:space-between;height:44px;align-items:center}
.nav li{font-size:14px;color:var(--white);padding:0 22px;height:44px;line-height:44px}
.nav li.active{background:#c7c7c7;color:var(--ink)}

.hero{position:absolute;top:176px;left:0;width:1200px;height:556px;background:linear-gradient(120deg,#4a4f57 0%,#7d838c 45%,#c9ccd1 100%)}
.hero-title{position:absolute;left:120px;top:280px;color:var(--white)}
.hero-title h1{font-size:52px;font-weight:700;letter-spacing:2px;line-height:64px}
.hero-title p{font-size:22px;font-weight:600;letter-spacing:2px;margin-top:4px}
.hero-title .bar{height:6px;width:370px;background:var(--orange);margin-top:8px}

/* welcome */
.welcome{position:absolute;top:732px;left:0;width:1200px;height:468px;padding-top:52px;text-align:center}
.section-title{font-size:40px;font-weight:400;color:var(--ink);line-height:52px}
.section-title b{color:var(--orange);font-weight:600}
.welcome .lead{width:820px;margin:14px auto 0;font-size:13px;line-height:22px;color:var(--muted)}
.services{display:flex;justify-content:space-between;margin-top:30px}
.service{width:240px;text-align:center}
.service .icon{width:100px;height:100px;border-radius:50%;background:#6c6c6c;margin:0 auto;display:flex;align-items:center;justify-content:center;border:6px solid #e6e6e6}
.service .icon i{width:46px;height:46px;border-radius:50%;background:var(--orange);display:block}
.service h3{font-size:14px;font-weight:600;margin-top:16px;line-height:20px;text-transform:uppercase}
.service p{font-size:12px;line-height:18px;color:var(--muted);margin-top:6px}

/* construction */
.construction{position:absolute;top:1200px;left:0;width:1200px;height:480px;background:var(--light);text-align:center}
.construction h2{font-size:30px;color:var(--orange);font-weight:700;margin-top:58px;letter-spacing:1px}
.construction .sub{font-size:16px;color:var(--ink);margin-top:4px}
.cards{display:flex;justify-content:space-between;margin-top:30px}
.card{width:316px;text-align:left}
.card .photo{height:168px}
.card .caption{background:var(--orange);color:var(--white);padding:10px 14px 12px;min-height:80px}
.card .caption h4{font-size:16px;font-weight:400}
.card .caption p{font-size:11px;line-height:16px;margin-top:4px;opacity:.9}

/* video + news */
.feature{position:absolute;top:1760px;left:80px;width:1040px;height:360px}
.video{position:absolute;left:20px;top:0;width:320px;height:300px;background:linear-gradient(160deg,#cfd6dc,#8e99a3)}
.play{position:absolute;left:130px;top:120px;width:60px;height:60px;border-radius:50%;background:rgba(0,0,0,.55)}
.feature-text{position:absolute;left:370px;top:0;width:300px}
.feature-text h3{font-size:17px;font-weight:400;line-height:24px;color:var(--ink)}
.feature-text p{font-size:12px;line-height:20px;color:var(--muted);margin-top:14px}
.news{position:absolute;left:720px;top:0;width:320px}
.news h3{font-size:17px;font-weight:600;text-transform:uppercase;padding-bottom:10px;border-bottom:1px solid var(--line)}
.news-item{display:flex;gap:16px;margin-top:22px}
.news-item .thumb{width:100px;height:90px;background:linear-gradient(150deg,#dfe5ea,#9aa6b1);flex:none}
.news-item h4{font-size:14px;color:var(--orange);font-weight:600}
.news-item .date{font-size:11px;color:var(--muted);margin-top:4px}
.news-item p{font-size:11px;line-height:17px;color:var(--muted);margin-top:4px}

/* reviews */
.divider{position:absolute;top:2160px;left:100px;width:1000px;height:1px;background:var(--line)}
.reviews{position:absolute;top:2190px;left:0;width:1200px;text-align:center}
.reviews .section-title{font-size:36px}
.review-row{display:flex;justify-content:space-between;width:980px;margin:40px auto 0;text-align:left}
.review{width:460px;display:flex;gap:22px}
.review .avatar{width:110px;height:110px;border-radius:50%;background:linear-gradient(160deg,#d9dde1,#7f8891);flex:none}
.review p{font-size:12px;line-height:20px;color:var(--muted)}
.review .stars{color:var(--orange);font-size:14px;margin-top:6px;letter-spacing:2px}
.review .who{font-size:12px;color:var(--orange);font-weight:600;margin-top:2px}

/* footer */
.footer{position:absolute;top:2480px;left:0;width:1200px;height:240px;background:var(--footer);color:#bdbdbd}
.footer .cols{display:flex;width:1040px;margin:0 auto;padding-top:40px;justify-content:space-between}
.fcol h5{font-size:14px;color:var(--white);font-weight:600;text-transform:uppercase;margin-bottom:12px}
.fcol li{list-style:none;font-size:11px;line-height:19px}
.fcol p{font-size:11px;line-height:19px}
.fbrand{width:220px}
.fbrand .brand-name{color:var(--white);font-size:22px}
.fbrand .socials{margin-top:18px}
.newsletter .form{display:flex;margin-top:14px}
.newsletter .field{width:170px;height:34px;background:var(--white);color:#999;font-size:11px;line-height:34px;padding-left:10px}
.newsletter .btn{width:100px;height:34px;background:var(--orange);color:var(--white);font-size:11px;line-height:34px;text-align:center;font-weight:600}
.copyright{position:absolute;top:2720px;left:0;width:1200px;height:32px;background:var(--footer-deep);color:#8a8a8a;font-size:11px;text-align:center;line-height:32px}
.to-top{position:absolute;right:60px;top:4px;width:24px;height:24px;background:#444}
</style>
</head>
<body>

<header class="topbar">
  <div class="wrap">
    <div class="brand"><span class="brand-dot"></span><span class="brand-name">TALVERO</span></div>
    <div class="top-right">
      <div class="socials"><span></span><span></span><span></span><span></span><span></span></div>
      <div class="contact-mini">
        <div class="phone"><svg width="14" height="14" viewBox="0 0 24 24"><path fill="#f07b1d" d="M6.6 10.8a15 15 0 006.6 6.6l2.2-2.2c.3-.3.7-.4 1-.2 1.1.4 2.3.6 3.6.6.6 0 1 .4 1 1V20c0 .6-.4 1-1 1A17 17 0 013 4c0-.6.4-1 1-1h3.5c.6 0 1 .4 1 1 0 1.3.2 2.5.6 3.6.1.3 0 .7-.2 1z"/></svg>(PH) 5550 1428</div>
        <div>info@talvero-eng.com</div>
      </div>
    </div>
  </div>
</header>

<nav class="nav">
  <div class="wrap">
    <ul>
      <li class="active">Home</li><li>About Us</li><li>Our Services</li><li>Project Controls</li><li>Structural</li><li>Drafting</li><li>Contact Us</li>
    </ul>
  </div>
</nav>

<section class="hero" role="img" aria-label="Engineer in a suit sketching a city skyline on a glass board">
  <div class="hero-title">
    <h1>ENGINEERING &amp;</h1>
    <div class="bar"></div>
    <p>MANAGEMENT SERVICES</p>
  </div>
</section>

<section class="welcome">
  <div class="wrap">
    <h2 class="section-title">Welcome To <b>Talvero</b></h2>
    <p class="lead">We deliver civil, structural and project expertise to clients across every stage of their build. Our team plans, designs and manages works with care, keeping budgets clear and schedules on track. From early concept to final handover we stay close to every detail, so each project is safe, efficient and built to last for the people who use it every day.</p>
    <div class="services">
      <div class="service"><div class="icon"><i></i></div><h3>Civil Engineering</h3><p>Roads, drainage and site works planned with care and delivered on time.</p></div>
      <div class="service"><div class="icon"><i></i></div><h3>Structural Engineering</h3><p>Sound frames and foundations designed for strength, safety and value.</p></div>
      <div class="service"><div class="icon"><i></i></div><h3>Project Management</h3><p>Clear plans, steady reporting and tight control of cost and time.</p></div>
      <div class="service"><div class="icon"><i></i></div><h3>Business Management</h3><p>Practical advice that helps firms grow and run projects smoothly.</p></div>
    </div>
  </div>
</section>

<section class="construction">
  <h2>CONSTRUCTION</h2>
  <p class="sub">Engineering And Management Services Company</p>
  <div class="wrap cards">
    <div class="card"><div class="photo" role="img" aria-label="Workers in hard hats on a site" style="background:linear-gradient(160deg,#9fc3e6,#e0c25a)"></div><div class="caption"><h4>Site Supervision</h4><p>Daily oversight that keeps crews safe and work moving forward.</p></div></div>
    <div class="card"><div class="photo" role="img" aria-label="Engineers reviewing plans in a building" style="background:linear-gradient(160deg,#b8c6d2,#d7a94a)"></div><div class="caption"><h4>Design Review</h4><p>Careful checks of drawings before any work begins on site.</p></div></div>
    <div class="card"><div class="photo" role="img" aria-label="Steel scaffolding on a building under construction" style="background:linear-gradient(160deg,#e3e6e9,#8f969c)"></div><div class="caption"><h4>Structural Works</h4><p>Strong frames raised to plan with quality at every level.</p></div></div>
  </div>
</section>

<section class="feature">
  <div class="video" role="img" aria-label="Video still of a smiling engineer in a hard hat"><span class="play"></span></div>
  <div class="feature-text">
    <h3>Practical engineering support for every project, large or small.</h3>
    <p>Our engineers bring years of field experience to each brief. We listen first, then plan works that suit your site, your budget and your timeline.</p>
    <p>We manage consultants, contractors and approvals in one place, giving you a single clear point of contact from start to finish and full reports as each stage is signed off.</p>
  </div>
  <div class="news">
    <h3>Latest News</h3>
    <div class="news-item"><div class="thumb" role="img" aria-label="Engineers on a site"></div><div><h4>New Bridge Project Begins</h4><div class="date">12 July 2015</div><p>Work starts on a new crossing for the region.</p></div></div>
    <div class="news-item"><div class="thumb" role="img" aria-label="Team meeting at a desk"></div><div><h4>Team Grows This Season</h4><div class="date">03 June 2015</div><p>Three new engineers join our design office.</p></div></div>
  </div>
</section>

<div class="divider"></div>

<section class="reviews">
  <h2 class="section-title">Customer <b>Reviews</b></h2>
  <div class="review-row">
    <div class="review"><div class="avatar" role="img" aria-label="Client portrait"></div><div><p>“The team kept our build on time and on budget. Clear reports every week and no surprises at handover. We will work with them again.”</p><div class="stars">★★★☆☆</div><div class="who">Client Name</div></div></div>
    <div class="review"><div class="avatar" role="img" aria-label="Client portrait"></div><div><p>“Sound advice from day one and a design that saved us real cost. Friendly, skilled and easy to reach whenever we had questions.”</p><div class="stars">★★★☆☆</div><div class="who">Client Name</div></div></div>
  </div>
</section>

<footer class="footer">
  <div class="cols">
    <div class="fcol fbrand">
      <div class="brand"><span class="brand-dot"></span><span class="brand-name">TALVERO</span></div>
      <div class="socials"><span></span><span></span><span></span><span></span><span></span></div>
    </div>
    <div class="fcol"><h5>Information</h5><ul><li>Civil Engineering</li><li>Structural Engineering</li><li>Project Management</li><li>Business Management</li><li>Project Controls</li></ul></div>
    <div class="fcol newsletter"><h5>Sign up for newsletter</h5><p>Get project news and updates<br>sent to your inbox each month.</p><div class="form"><div class="field">Enter Email</div><div class="btn">SUBSCRIBE</div></div></div>
    <div class="fcol"><h5>Contact Us</h5><p>Address:<br>PO Box 184, Riverton</p><p style="margin-top:8px">+1 555 014 2880<br>info@talvero-eng.com</p></div>
  </div>
</footer>
<div class="copyright">© 2015 TALVERO. All rights reserved.<span class="to-top"></span></div>

</body>
</html>
```